Ferncrest Dental, LLC business card project

Business card to be designed with current logo.
Dental office- please keep design of card that looks clean and professional.
Please include the following info:
Ferncrest Dental, LLC
Dr. Lorna Pettigrew
2871 Marlowe Street
Elmsford Glen, NV 89931
555-210-0193
ferncrestdental.office@examplemail.test
Hello everyone-
Reason: Just got back from overseas- will look at all designs and provide feedback. Thank you!
Reason: Polling my friends for the final selection-
thank you to all those that participated- so many talented designers!

```html
<!DOCTYPE html>
<html lang="en">
<head>
<meta charset="utf-8">
<title>Ferncrest Dental, LLC — Business Cards</title>
<link rel="stylesheet" href="https://fonts.googleapis.com/css2?family=Quicksand:wght@400&family=Arimo:wght@400;700&family=Roboto+Condensed:wght@400&display=swap">
<style>
  :root {
    --page: #ffffff;
    --card-dark: #2b2b2b;
    --card-grey: #6e6e6e;
    --lime: #b8cc16;
    --lime-soft: #d3e06a;
    --olive: #8a9a1c;
    --leaf: #6a9e2e;
    --text-grey: #6b6b6b;
    --paper: #ffffff;
  }
  html, body {
    margin: 0;
    padding: 0;
    width: 882px;
    height: 1200px;
    overflow: hidden;
    background: var(--page);
  }
  .sheet { position: relative; width: 882px; height: 1200px; }
  .card {
    position: absolute;
    width: 860px;
    height: 536px;
    border-radius: 28px;
    overflow: hidden;
  }
  .card--front { left: 21px; top: 2px; background: var(--card-dark); }
  .card--back  { left: 2px;  top: 662px; background: var(--paper); }
  .card__art { position: absolute; inset: 0; width: 860px; height: 536px; }
  .brand-dot {
    position: absolute;
    left: 112px;
    top: 70px;
    width: 36px;
    height: 36px;
    border-radius: 50%;
    background: var(--lime);
  }
  .brand {
    position: absolute;
    left: 170px;
    top: 66px;
    margin: 0;
    font-family: "Quicksand", sans-serif;
    font-weight: 400;
    font-size: 46px;
    line-height: 1;
    color: var(--leaf);
    white-space: nowrap;
  }
  .doctor {
    position: absolute;
    left: 177px;
    top: 276px;
    margin: 0;
    font-family: "Arimo", sans-serif;
    font-weight: 400;
    font-size: 37px;
    line-height: 1;
    white-space: nowrap;
  }
  .card--front .doctor { color: var(--leaf); }
  .card--back .doctor { color: var(--text-grey); }
  .contact {
    position: absolute;
    left: 440px;
    top: 376px;
    margin: 0;
    font-family: "Roboto Condensed", sans-serif;
    font-style: normal;
    font-size: 26px;
    line-height: 32px;
    white-space: nowrap;
  }
  .card--front .contact { color: var(--leaf); }
  .card--back .contact { color: var(--text-grey); }
  .contact__company {
    display: block;
    font-family: "Arimo", sans-serif;
    font-weight: 700;
    font-size: 22px;
    line-height: 28px;
  }
  .contact__line { display: block; }
  .contact__email { display: block; font-size: 24px; line-height: 32px; }
</style>
</head>
<body>
<main class="sheet">

  <section class="card card--front" aria-label="Business card, dark version">
    <svg class="card__art" viewBox="0 0 860 536" aria-hidden="true">
      <rect class="block block--right" x="770" y="120" width="140" height="300" rx="24" fill="var(--olive)"/>
      <rect class="block block--right-inner" x="800" y="150" width="110" height="240" rx="20" fill="var(--lime)"/>
      <rect class="block block--left" x="-60" y="250" width="120" height="240" rx="22" fill="var(--olive)"/>
      <rect class="name-rule" x="177" y="330" width="240" height="4" rx="2" fill="var(--lime)"/>
    </svg>
    <span class="brand-dot" aria-hidden="true"></span>
    <h1 class="brand">Ferncrest Dental, LLC</h1>
    <h2 class="doctor">Dr. Lorna Pettigrew</h2>
    <address class="contact">
      <span class="contact__company">Ferncrest Dental, LLC</span>
      <span class="contact__line">2871 Marlowe Street</span>
      <span class="contact__line">Elmsford Glen, NV 89931</span>
      <span class="contact__line">555-210-0193</span>
      <span class="contact__email">ferncrestdental.office@examplemail.test</span>
    </address>
  </section>

  <section class="card card--back" aria-label="Business card, light version">
    <svg class="card__art" viewBox="0 0 860 536" aria-hidden="true">
      <polygon class="panel-grey" points="0,0 860,0 860,250 0,170" fill="var(--card-grey)"/>
      <polygon class="edge-stripe" points="0,170 860,250 860,262 0,182" fill="var(--lime)"/>
      <rect class="block block--right" x="780" y="300" width="130" height="200" rx="22" fill="var(--lime-soft)"/>
      <rect class="block block--left" x="-60" y="250" width="120" height="240" rx="22" fill="var(--lime-soft)"/>
      <rect class="name-rule" x="177" y="330" width="240" height="4" rx="2" fill="var(--lime)"/>
    </svg>
    <span class="brand-dot" aria-hidden="true"></span>
    <h1 class="brand">Ferncrest Dental, LLC</h1>
    <h2 class="doctor">Dr. Lorna Pettigrew</h2>
    <address class="contact">
      <span class="contact__company">Ferncrest Dental, LLC</span>
      <span class="contact__line">2871 Marlowe Street</span>
      <span class="contact__line">Elmsford Glen, NV 89931</span>
      <span class="contact__line">555-210-0193</span>
      <span class="contact__email">ferncrestdental.office@examplemail.test</span>
    </address>
  </section>

</main>
</body>
</html>
```